Product label for herbal salves, lotions, soaps and tinctures

We need a very simple, clean and organic looking label that can be used for an ointment jar, a lotion bottle and a dropper bottle.
We have an existing logo (see attached). We like the colors white, olive green, gold and black. It needs to include product name as dominant and logo. It also needs to include an ingredient list, and usage statement. Include weight of product, distributed by, made in the USA, and NQB statement.
Example of what needs to be present:
Logo
Name: Calmwick Balm
Used for: For Muscle Aches, Arthritis, Tendonitis, Headaches
To Use: For muscle aches, arthritis and tendonitis, massage into affected area. For tension headache apply to neck, temples and forehead.
Store in a cool and dry place, away from direct heat and sunlight.
Weight of product: 1.75
DIST. BY: Brookmere Herbal
Made in the USA
This product is not intended to diagnose, treat, cure
or prevent any disease. Not regulated
by the NQB. Please consult your health care practitioner
before using product. Discontinue use if any adverse reaction occurs.
Ingredient list:
Wildcrafted Ingredients:
Ashwagandha Root, Peppermint Leaf, Hops Flowers, St. John’s Wort Herb, Arnica Flowers, Green Tea Leaf, Alfalfa Leaf, Dandelion Root, Burdock Root, Chickweed Herb, Chaparral Leaf, Yarrow Flowers, Boneset Herb, Moringa Leaf, Meadowsweet Herb, Nettle Leaf
Organic Ingredients:
Olive Oil, Aloe Leaf, Sweet Birch Bark, Helichrysum Flowers, Holy Basil Leaf, Borage Herb, Ginger Root, Angelica Root, White Willow Bark, Mustard Seed, Beeswax, Vitamin E, Essential Oils
Dimensions of Jar:
Circumference: 7 in.
Height: 1 in.

```html
<!DOCTYPE html>
<html lang="en">
<head>
<meta charset="utf-8">
<title>Brookmere Herbal – Calmwick Balm Jar Label</title>
<link rel="stylesheet" href="https://fonts.googleapis.com/css2?family=Arimo:wght@400;700&display=swap">
<style>
  :root {
    --canvas: #fefefe;
    --frame: #333333;
    --label: #e4c19f;
    --ink: #333333;
    --olive: #6b7330;
    --marker: #e0322c;
  }
  html, body {
    margin: 0;
    padding: 0;
    width: 1200px;
    height: 1200px;
    overflow: hidden;
    background: var(--canvas);
  }
  .sheet {
    position: relative;
    width: 1200px;
    height: 1200px;
    box-sizing: border-box;
    border: 1px solid var(--frame);
    font-family: "Arimo", Arial, sans-serif;
    color: var(--ink);
  }
  .dimension-lines {
    position: absolute;
    left: 0;
    top: 0;
  }
  .dimension-label {
    position: absolute;
    font-size: 22px;
    line-height: 1;
    color: var(--ink);
    white-space: nowrap;
  }
  .dimension-width { left: 545px; top: 502px; }
  .dimension-height {
    left: 1140px;
    top: 620px;
    font-size: 12.5px;
    transform: translate(-50%, -50%) rotate(-90deg);
  }
  .jar-label {
    position: absolute;
    left: 57px;
    top: 545px;
    width: 1049px;
    height: 150px;
    background: var(--label);
  }
  .ingredients {
    position: absolute;
    left: 40px;
    top: 7px;
    width: 330px;
    text-align: center;
    font-size: 10px;
    line-height: 11.7px;
    white-space: nowrap;
  }
  .ingredients .heading { font-weight: 700; }
  .brand-block {
    position: absolute;
    left: 374px;
    top: 0;
    width: 300px;
    height: 150px;
    text-align: center;
  }
  .brand-name {
    position: absolute;
    left: 0;
    right: 0;
    top: 56px;
    font-size: 25px;
    font-weight: 700;
    color: var(--olive);
    line-height: 1;
  }
  .net-weight {
    position: absolute;
    left: 0;
    right: 0;
    top: 133px;
    font-size: 10px;
    font-weight: 700;
    line-height: 1;
  }
  .product-details {
    position: absolute;
    left: 694px;
    top: 8px;
    width: 350px;
    font-size: 8.3px;
    line-height: 9.2px;
    white-space: nowrap;
  }
  .product-details p { margin: 0; }
  .product-details b { font-weight: 700; }
  .storage-note {
    display: inline-block;
    outline: 0.8px solid var(--marker);
    outline-offset: 0.5px;
    padding: 0 1px;
    margin-left: -2px;
  }
  .disclaimer { margin-top: 4.5px !important; }
  .distribution {
    margin-top: 6px !important;
    padding-left: 1px;
    font-weight: 700;
    line-height: 10px;
  }
</style>
</head>
<body>
<main class="sheet">
  <svg class="dimension-lines" width="1200" height="1200" viewBox="0 0 1200 1200" aria-hidden="true">
    <g fill="#333333" stroke="#333333">
      <line x1="64" y1="524" x2="1098" y2="524" stroke-width="1"/>
      <path d="M57 524 L72 518 L69 524 L72 530 Z" stroke="none"/>
      <path d="M1106 524 L1091 518 L1094 524 L1091 530 Z" stroke="none"/>
      <line x1="1129" y1="552" x2="1129" y2="688" stroke-width="1"/>
      <path d="M1129 545 L1123 559 L1129 556 L1135 559 Z" stroke="none"/>
      <path d="M1129 695 L1123 681 L1129 684 L1135 681 Z" stroke="none"/>
    </g>
  </svg>
  <span class="dimension-label dimension-width">7 INCH</span>
  <span class="dimension-label dimension-height">1 INCH</span>

  <section class="jar-label">
    <div class="ingredients">
      <div class="heading">Ingredient list :</div>
      <div>Wildcrafted Ingredients:</div>
      <div>Ashwagandha Root, Peppermint Leaf, Hops Flowers,</div>
      <div>St. John’s Wort Herb, Arnica Flowers, Green Tea Leaf,</div>
      <div>Alfalfa Leaf, Dandelion Root, Burdock Root, Chickweed Herb,</div>
      <div>Chaparral Leaf, Yarrow Flowers, Boneset Herb, Moringa Leaf,</div>
      <div>Meadowsweet Herb, Nettle Leaf</div>
      <div class="heading">Organic Ingredients :</div>
      <div>Olive Oil, Aloe Leaf, Sweet Birch Bark, Helichrysum Flowers,</div>
      <div>Holy Basil Leaf, Borage Herb, Ginger Root, Angelica Root,</div>
      <div>White Willow Bark, Mustard Seed, Beeswax, Vitamin E, Essential Oils</div>
    </div>

    <div class="brand-block">
      <div class="brand-name">Brookmere Herbal</div>
      <div class="net-weight">Weight of product: 1.75</div>
    </div>

    <div class="product-details">
      <p><b>Name :</b> Calmwick Balm</p>
      <p><b>Used for :</b> For Muscle Aches, Arthritis, Tendonitis, Headaches</p>
      <p><b>To Use :</b> For muscle aches, arthritis and tendonitis, massage<br>into affected area. For tension headache apply to neck, temples<br>and forehead.</p>
      <p><span class="storage-note">Store in a cool and dry place, away from direct heat and sunlight.</span></p>
      <p class="disclaimer">This product is not intended to diagnose, treat, cure<br>or prevent any disease. Not regulated by the NQB.<br>Please consult your health care practitioner before<br>using product. Discontinue use if any adverse reaction<br>occurs.</p>
      <p class="distribution">DIST. BY: Brookmere Herbal<br>Made in the USA</p>
    </div>
  </section>
</main>
</body>
</html>
```